Business cards for KORU Real Estate Holdings LLC

We need a cool, original business card design for a company based in the Washington DC metropolitan area. We are a new energetic and passionate Real Estate Investing Company that invests in all types of real estate; commercial, residential, industrial etc.

Our company color is Red since it reflects action, energy and speed; it is assertive confident, energizing, exciting, powerful, passionate and determined. So we would like business card communicate those qualities to the audience.

Our audiences are investors that want to invest with us, real estate sellers, buyers, and tenants who lease from us.

Our logo is attached

```html
<!DOCTYPE html>
<html lang="en">
<head>
<meta charset="utf-8">
<title>KORU Real Estate Holdings LLC – Business Cards</title>
<link rel="stylesheet" href="https://fonts.googleapis.com/css2?family=Oswald:wght@400;500;600&family=Open+Sans:wght@400;600&display=swap">
<style>
  :root {
    --backdrop: #1c1c1d;
    --card-white: #ffffff;
    --card-shade: #ececec;
    --ink-dark: #3a3a3c;
    --ink-mid: #55565a;
    --brand-red: #d8333a;
    --band-dark: #343436;
    --band-text: #f2f2f2;
  }
  * { margin: 0; padding: 0; box-sizing: border-box; }
  html, body { width: 1200px; height: 864px; overflow: hidden; }
  body { background: var(--backdrop); position: relative; font-family: "Open Sans", sans-serif; }

  .card {
    position: absolute;
    width: 720px;
    height: 412px;
    background: linear-gradient(160deg, var(--card-white) 0%, var(--card-white) 55%, var(--card-shade) 100%);
    box-shadow: 0 18px 40px rgba(0,0,0,.55);
    overflow: hidden;
  }
  .card--front { left: 80px; top: 50px; }
  .card--back { left: 400px; top: 400px; }

  .brand {
    position: absolute;
    display: flex;
    align-items: center;
    gap: 16px;
  }
  .brand__dot {
    flex: none;
    border-radius: 50%;
    background: var(--brand-red);
  }
  .brand__name {
    font-family: "Oswald", sans-serif;
    font-weight: 600;
    color: var(--ink-dark);
    text-transform: uppercase;
    line-height: 1.1;
    letter-spacing: 1px;
  }
  .card--front .brand { left: 190px; top: 150px; }
  .card--front .brand__dot { width: 56px; height: 56px; }
  .card--front .brand__name { font-size: 34px; width: 300px; }

  .card--back .brand { right: 50px; top: 60px; }
  .card--back .brand__dot { width: 36px; height: 36px; }
  .card--back .brand__name { font-size: 22px; width: 200px; }

  .back-band { position: absolute; left: 0; top: 0; width: 720px; height: 412px; }
  .band-dark { fill: var(--band-dark); }
  .band-red { fill: var(--brand-red); }

  .person { position: absolute; left: 46px; top: 190px; }
  .person__name {
    font-family: "Oswald", sans-serif;
    font-weight: 500;
    font-size: 28px;
    color: var(--ink-dark);
    letter-spacing: 1px;
    line-height: 1;
  }
  .person__role {
    font-family: "Oswald", sans-serif;
    font-weight: 400;
    font-size: 13px;
    color: var(--ink-mid);
    letter-spacing: 1.5px;
    margin-top: 4px;
  }
  .contact { list-style: none; position: absolute; left: 46px; top: 270px; }
  .contact__item {
    display: flex; align-items: center; gap: 10px;
    font-size: 11.5px; color: var(--ink-mid);
    height: 21px;
  }
  .contact__icon { width: 12px; height: 12px; fill: var(--ink-dark); flex: none; }

  .address {
    position: absolute; right: 34px; top: 312px;
    font-family: "Oswald", sans-serif;
    font-size: 15px; letter-spacing: .5px;
    color: var(--band-text);
  }
</style>
</head>
<body>

<section class="card card--front" aria-label="Business card front">
  <div class="brand">
    <span class="brand__dot"></span>
    <span class="brand__name">KORU Real Estate Holdings LLC</span>
  </div>
</section>

<section class="card card--back" aria-label="Business card back">
  <svg class="back-band" viewBox="0 0 720 412" aria-hidden="true">
    <path class="band-red" d="M0 392 H262 C294 392 290 288 324 288 H720 V300 H332 C300 300 302 400 270 400 H0 Z"/>
    <path class="band-dark" d="M0 400 H270 C302 400 300 300 332 300 H720 V412 H0 Z"/>
  </svg>

  <div class="brand">
    <span class="brand__dot"></span>
    <span class="brand__name">KORU Real Estate Holdings LLC</span>
  </div>

  <div class="person">
    <p class="person__name">DANIEL REYES</p>
    <p class="person__role">GENERAL MANAGER</p>
  </div>

  <ul class="contact">
    <li class="contact__item">
      <svg class="contact__icon" viewBox="0 0 12 12"><path d="M2.5 0.5 L4.5 0.5 L5 3.5 L3.6 4.4 C4.3 6 5.9 7.6 7.6 8.4 L8.5 7 L11.5 7.5 L11.5 9.5 C11.5 10.6 10.6 11.5 9.5 11.5 C4.5 11.2 0.8 7.5 0.5 2.5 C0.5 1.4 1.4 0.5 2.5 0.5 Z"/></svg>
      202 555 0147
    </li>
    <li class="contact__item">
      <svg class="contact__icon" viewBox="0 0 12 12"><path d="M3.5 0 H8.5 A1 1 0 0 1 9.5 1 V11 A1 1 0 0 1 8.5 12 H3.5 A1 1 0 0 1 2.5 11 V1 A1 1 0 0 1 3.5 0 Z M3.7 1.5 V9.5 H8.3 V1.5 Z"/></svg>
      202 555 0183
    </li>
    <li class="contact__item">
      <svg class="contact__icon" viewBox="0 0 12 12"><path d="M3 0.5 H9 V3.5 H3 Z M1 4.5 H11 V9 H9 V11.5 H3 V9 H1 Z M4 7.5 V10.5 H8 V7.5 Z"/></svg>
      202 555 0190
    </li>
    <li class="contact__item">
      <svg class="contact__icon" viewBox="0 0 12 12"><path d="M0.5 2 H11.5 V10 H0.5 Z M1.5 3 L6 6.5 L10.5 3 Z"/></svg>
      d.reyes@koruholdings.com
    </li>
    <li class="contact__item">
      <svg class="contact__icon" viewBox="0 0 12 12"><path d="M6 0.5 A5.5 5.5 0 1 0 6 11.5 A5.5 5.5 0 1 0 6 0.5 Z M6 1.6 C6.8 2.4 7.3 3.8 7.4 5.4 H4.6 C4.7 3.8 5.2 2.4 6 1.6 Z M4.6 6.6 H7.4 C7.3 8.2 6.8 9.6 6 10.4 C5.2 9.6 4.7 8.2 4.6 6.6 Z M1.7 5.4 C1.9 3.6 3 2.2 4.4 1.7 C3.8 2.7 3.5 4 3.4 5.4 Z M8.6 5.4 C8.5 4 8.2 2.7 7.6 1.7 C9 2.2 10.1 3.6 10.3 5.4 Z M1.7 6.6 H3.4 C3.5 8 3.8 9.3 4.4 10.3 C3 9.8 1.9 8.4 1.7 6.6 Z M8.6 6.6 H10.3 C10.1 8.4 9 9.8 7.6 10.3 C8.2 9.3 8.5 8 8.6 6.6 Z"/></svg>
      www.koruholdings.com
    </li>
  </ul>

  <p class="address">450 Harbor Lane, Suite 3, Washington DC</p>
</section>

</body>
</html>
```